Modernise Business Card

Our company has been operating for 10 years. With the start of the new decade we are looking to refresh our business card design. We manufacture a range of industrial product shipping to customers internationally. A copy of our current card, both sides, is attached. We are looking for a mature professional appearance.

```html
<!DOCTYPE html>
<html lang="en">
<head>
<meta charset="utf-8">
<title>Business Card – Front and Back</title>
<link href="https://fonts.googleapis.com/css2?family=Open+Sans:wght@300;400;600;700;800&display=swap" rel="stylesheet">
<style>
  :root {
    --page: #ffffff;
    --card: #1c1c1c;
    --ink: #ffffff;
    --accent: #1b9ad6;
  }
  * { box-sizing: border-box; margin: 0; padding: 0; }
  html, body {
    width: 1200px; height: 1200px; overflow: hidden;
    background: var(--page);
    font-family: "Open Sans", Arial, sans-serif;
  }
  .sheet {
    position: relative; width: 1200px; height: 1200px;
  }
  .card {
    position: absolute; top: 432px;
    width: 560px; height: 336px;
    background: var(--card); color: var(--ink);
  }
  .card--front { left: 32px; }
  .card--back { left: 608px; }

  .holder-name {
    position: absolute; left: 79px; top: 56px;
    font-weight: 400; font-size: 27px; letter-spacing: 0.2px;
  }
  .rule {
    position: absolute; height: 4px; background: var(--accent);
  }
  .front-rule-left { left: 0; top: 117px; width: 308px; }
  .front-rule-right { left: 490px; top: 117px; width: 70px; }
  .logo-word {
    position: absolute; font-weight: 700; text-transform: uppercase; white-space: nowrap;
    line-height: 1;
  }
  .front-logo { left: 327px; top: 112px; font-size: 15px; letter-spacing: 0.9px; }

  .contact {
    position: absolute; left: 57px; top: 160px;
    font-size: 10.5px; line-height: 13px; font-weight: 600;
  }
  .contact-group { display: flex; gap: 9px; margin-bottom: 4px; }
  .contact-icon { width: 13px; height: 13px; flex: none; margin-top: 1px; }
  .contact-row { display: flex; }
  .contact-row .label { width: 71px; }

  .back-rule-left { left: 0; top: 165px; width: 131px; }
  .back-rule-right { left: 425px; top: 165px; width: 135px; }
  .back-logo {
    left: 0; width: 560px; text-align: center; top: 155px;
    font-size: 23px; letter-spacing: 2px;
  }
</style>
</head>
<body>
<main class="sheet">
  <section class="card card--front" aria-label="Card front">
    <h1 class="holder-name">Ross Whitfield</h1>
    <div class="rule front-rule-left"></div>
    <div class="logo-word front-logo">Your Logo Here</div>
    <div class="rule front-rule-right"></div>

    <div class="contact">
      <div class="contact-group">
        <svg class="contact-icon" viewBox="0 0 13 13" aria-hidden="true">
          <rect width="13" height="13" rx="2" fill="var(--accent)"/>
          <rect x="2.5" y="3.8" width="8" height="5.6" fill="none" stroke="#1c1c1c" stroke-width="1"/>
          <path d="M2.5 3.8 L6.5 7 L10.5 3.8" fill="none" stroke="#1c1c1c" stroke-width="1"/>
        </svg>
        <div>
          <div>Email : rwhitfield@kelvarfittings.com</div>
          <div>Web &nbsp;: www.kelvarfittings.com</div>
        </div>
      </div>
      <div class="contact-group">
        <svg class="contact-icon" viewBox="0 0 13 13" aria-hidden="true">
          <rect width="13" height="13" rx="2" fill="var(--accent)"/>
          <path d="M4 3 L5.6 4.6 L4.8 5.8 Q5.8 7.6 7.2 8.2 L8.4 7.4 L10 9 L8.8 10.2 Q5.4 9.6 2.8 4.2 Z" fill="#1c1c1c"/>
        </svg>
        <div>
          <div class="contact-row"><span class="label">China</span><span>: +86 155 2074 9618</span></div>
          <div class="contact-row"><span class="label">Australia</span><span>: +61 402 735 118</span></div>
        </div>
      </div>
      <div class="contact-group">
        <svg class="contact-icon" viewBox="0 0 13 13" aria-hidden="true">
          <rect width="13" height="13" rx="2" fill="var(--accent)"/>
          <path d="M2.5 6.6 L6.5 3 L10.5 6.6 M3.8 5.6 V10 H9.2 V5.6" fill="none" stroke="#1c1c1c" stroke-width="1"/>
        </svg>
        <div>
          <div>Address :</div>
          <div>1207-3,Lian Feng Building</div>
          <div>146 Qiaomen Road, Haishu District</div>
          <div>Ningbo 315010 China</div>
        </div>
      </div>
    </div>
  </section>

  <section class="card card--back" aria-label="Card back">
    <div class="rule back-rule-left"></div>
    <div class="logo-word back-logo">Your Logo Here</div>
    <div class="rule back-rule-right"></div>
  </section>
</main>
</body>
</html>
```